Need App for Impact Related Events

My app is to help with internal events. When you enter the prompted event code the next screen shows you everyone currently at the event. It will give you the ability to Start a conversation with someone you met at that event, or signal it is your turn to send a message. The next screen is a message thread with that person. I am looking for a design that incorporates the colors and ‘feel good’ emotion of our logo. I have pieced together a pretty good interpretation of what I’m looking for in the attached mockup by slicing and dicing designs. I also attached our logo mascot.Screens (see attached mockups)

Note 1: I do not like the picture on the screen used in screen one because it makes it seem like a dating app. I attached an alternative photo that can be used or present different ideas.

Note 2: On the login/signup screen (screen 2) I need an additional first and last name for login, you can try to fit this on one login screen or present a two step signup screen where that is presented in the second screen.

READ MOCKUP GUIDELINES UNDER Must Haves

Target Market(s)

People attending internal social impact events

Industry/Entity Type

Charity

Font styles to use
Sans Serif

Colors
86cfc6

Requirements
Must have
• Follow the screen mockups attached to project
• PLEASE READ
• I have provided a relatively close design of what I’m looking for in the mockups. Some screens need to be followed more closely to my design mockup than other. I have listed a guide below how how closely you should follow my mockup design exactly. Overall I would like to see some ideas of incorporating a few accent colors so it doesn’t appear SO Blue. I also attached some app inspiration designs I found from around the web
• Screen Mockup Guideline Follow %
• Screen 1: 65% - mostly on target, would like to see ways to make it not SO Blue and possibly creative places to add some explainer text describing the app
• Screen 2: 50% - general design idea is here, but more open
• Screen 3: 35% - a lot more room for design influence
• Screen 4: 70% - mostly on target, a little room for design influence/color scheme ideas
• Screen 5-6: 25% - a lot of room for design change/ideas/influence
• Screen 7-8: 80% - already very close to what I need, maybe open to slight sizing and color scheme ideas
• Screen 9: 15% - the most open for influence, only the general functionality of the screen is communicated here
Nice to have
• Please Read Mockup Guideline above. In large part I am looking for something to use some nice accent colors so it is not overwhelmingly blue and bring the whole design into a seamless style.
Should not have

```html
<!DOCTYPE html>
<html lang="en">
<head>
<meta charset="utf-8">
<title>Event Chat – Message Thread</title>
<link rel="stylesheet" href="https://fonts.googleapis.com/css2?family=Montserrat:ital,wght@0,400;0,500;0,600;0,700;1,400&display=swap">
<style>
  :root {
    --teal: #22c5c4;
    --teal-soft: #e5f8f7;
    --ink: #1d1d1f;
    --muted: #8a8f94;
    --line: #e4e7ea;
    --field-border: #cfd8dc;
    --avatar-a: #7b8fa0;
    --avatar-b: #b08a74;
    --surface: #ffffff;
  }
  * { box-sizing: border-box; margin: 0; padding: 0; }
  html, body { width: 1200px; height: 2281px; overflow: hidden; background: var(--surface); }
  body { position: relative; font-family: "Montserrat", sans-serif; color: var(--ink); }

  .abs { position: absolute; }

  .back-button { left: 130px; top: 130px; width: 90px; height: 60px; }
  .settings-button { left: 990px; top: 128px; width: 64px; height: 64px; }

  .contact-name { right: 370px; top: 310px; font-size: 50px; font-weight: 700; letter-spacing: -0.5px; }
  .contact-status { right: 370px; top: 378px; font-size: 24px; font-weight: 600; color: var(--teal); }

  .avatar { border-radius: 50%; }
  .avatar--contact { background: linear-gradient(135deg, var(--avatar-a), #4e5f6c); }
  .avatar--me { background: linear-gradient(135deg, var(--avatar-b), #6d4f3f); }
  .avatar--header { left: 855px; top: 258px; width: 184px; height: 184px; border: 8px solid var(--surface); box-shadow: 0 6px 24px rgba(0,0,0,0.08); }

  .divider { left: 0; top: 500px; width: 1200px; height: 3px; background: var(--line); }

  .bubble { font-size: 28px; font-weight: 700; line-height: 1.6; display: flex; align-items: center; }
  .bubble--in { background: var(--teal-soft); color: var(--teal); border-radius: 55px; padding: 0 48px; }
  .bubble--out { background: var(--teal); color: var(--surface); border-radius: 90px 90px 20px 90px; padding: 0 56px; }

  .msg-time { font-size: 22px; color: var(--muted); font-weight: 500; }

  .avatar--m1 { left: 156px; top: 650px; width: 120px; height: 120px; }
  .bubble--m1 { left: 324px; top: 660px; width: 518px; height: 110px; }
  .time--m1 { left: 748px; top: 798px; }

  .avatar--m2 { left: 916px; top: 1018px; width: 124px; height: 124px; }
  .bubble--m2 { left: 313px; top: 1000px; width: 611px; height: 180px; }
  .time--m2 { left: 400px; top: 1200px; }

  .avatar--m3 { left: 156px; top: 1390px; width: 120px; height: 120px; }
  .bubble--m3 { left: 324px; top: 1395px; width: 518px; height: 110px; }
  .seen { left: 670px; top: 1525px; display: flex; align-items: center; gap: 16px; }
  .avatar--seen { width: 40px; height: 40px; }

  .typing { left: 148px; top: 1885px; display: flex; align-items: center; gap: 22px; }
  .avatar--typing { width: 60px; height: 60px; }
  .typing-icon { width: 80px; height: 70px; }

  .composer { left: 97px; top: 2088px; width: 900px; height: 96px; border: 3px solid var(--field-border); border-radius: 48px; display: flex; align-items: center; padding-left: 40px; gap: 26px; }
  .composer-clip { width: 40px; height: 40px; }
  .composer-placeholder { font-size: 26px; font-style: italic; color: #5a5f64; }

  .send-button { left: 875px; top: 2048px; width: 170px; height: 170px; border-radius: 50%; background: var(--teal); box-shadow: 0 10px 30px rgba(34,197,196,0.35); display: flex; align-items: center; justify-content: center; }
  .send-icon { width: 78px; height: 78px; }
</style>
</head>
<body>
  <header>
    <svg class="abs back-button" viewBox="0 0 90 60" aria-label="Back">
      <path d="M86 30H10M34 6L10 30l24 24" fill="none" stroke="var(--teal)" stroke-width="8" stroke-linecap="round" stroke-linejoin="round"/>
    </svg>
    <svg class="abs settings-button" viewBox="0 0 24 24" aria-label="Settings">
      <path fill="var(--teal)" d="M19.4 13a7.6 7.6 0 0 0 0-2l2.1-1.6-2-3.5-2.5 1a7.4 7.4 0 0 0-1.7-1L15 3.2h-4l-.4 2.7a7.4 7.4 0 0 0-1.7 1l-2.5-1-2 3.5L6.6 11a7.6 7.6 0 0 0 0 2l-2.1 1.6 2 3.5 2.5-1a7.4 7.4 0 0 0 1.7 1l.4 2.7h4l.4-2.7a7.4 7.4 0 0 0 1.7-1l2.5 1 2-3.5L19.4 13zM13 15.5a3.5 3.5 0 1 1 0-7 3.5 3.5 0 0 1 0 7z" transform="translate(-1 0)"/>
    </svg>
    <h1 class="abs contact-name">Marcus Hale</h1>
    <p class="abs contact-status">Online</p>
    <div class="abs avatar avatar--contact avatar--header" role="img" aria-label="Profile photo of Marcus Hale"></div>
  </header>
  <div class="abs divider"></div>

  <main class="thread">
    <div class="abs avatar avatar--contact avatar--m1" role="img" aria-label="Profile photo of Marcus Hale"></div>
    <p class="abs bubble bubble--in bubble--m1">Hey, How was meet up</p>
    <span class="abs msg-time time--m1">9:45 pm</span>

    <p class="abs bubble bubble--out bubble--m2">Do you want to know more...?<br>I met nice girls who willing to help</p>
    <div class="abs avatar avatar--me avatar--m2" role="img" aria-label="Your profile photo"></div>
    <span class="abs msg-time time--m2">9:51 pm</span>

    <div class="abs avatar avatar--contact avatar--m3" role="img" aria-label="Profile photo of Marcus Hale"></div>
    <p class="abs bubble bubble--in bubble--m3">That is awesome. Yes shoot me</p>
    <div class="abs seen">
      <div class="avatar avatar--contact avatar--seen" role="img" aria-label="Seen by Marcus Hale"></div>
      <span class="msg-time">Seen</span>
    </div>

    <div class="abs typing">
      <div class="avatar avatar--contact avatar--typing" role="img" aria-label="Marcus Hale is typing"></div>
      <svg class="typing-icon" viewBox="0 0 80 70" aria-hidden="true">
        <path d="M14 6h52a8 8 0 0 1 8 8v30a8 8 0 0 1-8 8H30l-14 12v-12h-2a8 8 0 0 1-8-8V14a8 8 0 0 1 8-8z" fill="none" stroke="var(--teal)" stroke-width="5" stroke-linejoin="round"/>
        <circle cx="26" cy="29" r="5" fill="var(--teal)"/>
        <circle cx="40" cy="29" r="5" fill="var(--teal)"/>
        <circle cx="54" cy="29" r="5" fill="var(--teal)"/>
      </svg>
    </div>
  </main>

  <footer>
    <div class="abs composer">
      <svg class="composer-clip" viewBox="0 0 24 24" aria-hidden="true">
        <path d="M20 11.5l-8.2 8.2a5 5 0 0 1-7.1-7.1l8.5-8.5a3.3 3.3 0 0 1 4.7 4.7l-8.5 8.5a1.7 1.7 0 0 1-2.4-2.4l7.8-7.8" fill="none" stroke="var(--teal)" stroke-width="2" stroke-linecap="round" stroke-linejoin="round"/>
      </svg>
      <span class="composer-placeholder">Type something here...</span>
    </div>
    <div class="abs send-button" aria-label="Send">
      <svg class="send-icon" viewBox="0 0 24 24" aria-hidden="true">
        <path d="M21 3L3 10.5l7 2.5 2.5 7L21 3z" fill="none" stroke="#fff" stroke-width="2" stroke-linejoin="round"/>
        <path d="M10 13l5-5" stroke="#fff" stroke-width="2" stroke-linecap="round"/>
      </svg>
    </div>
  </footer>
</body>
</html>
```